New business card with our logo

we finalized our logo with the help of pixel harbor - now we need a business card using that logo. we are a metal service center providing raw steel and metal products for fabricating, contractors, artists, etc. we have the wording for the back of the card figured out (attached, no deviations from text please), just need help putting it all together.
would like the look of steel somehow incorporated in the design ... would like the black part of the logo to be steel or silver color (the S & BRANLEY)
Other font styles liked:
- calibri, arial, similar to those, modern looking
Colors
Designer to choose colors to be used in the design.
Requirements
Must have
- Back of card must haves are attached (no deviations from wording please).
- FRONT of card:
- logo
- address
- name
- office tel
- cell
- fax
- website
- address
Nice to have
- incorporate the look of steel or element of steel somehow
- names of the staff on front not in all caps, i.e. Rosvita not ROSVITA
- this industry is more industrial, not coffee or flower shop so design should be aligned with that
- design should be classic and tasteful

```html
<!DOCTYPE html>
<html lang="en">
<head>
<meta charset="utf-8">
<title>Branley Steel – Business Card</title>
<link href="https://fonts.googleapis.com/css2?family=Arimo:wght@400;700&display=swap" rel="stylesheet">
<style>
  :root {
    --blue: #0b72b9;
    --steel-dark: #333539;
    --paper: #ffffff;
    --backdrop: #e6e7e9;
    --ink: #2b2c2e;
  }
  * { box-sizing: border-box; margin: 0; padding: 0; }
  html, body {
    width: 1200px; height: 880px; overflow: hidden;
    background: var(--backdrop);
    font-family: "Arimo", Arial, sans-serif;
  }
  .sheet {
    width: 1200px; height: 880px;
    display: flex; flex-direction: column; align-items: center; justify-content: center;
    gap: 40px;
  }
  .card {
    position: relative;
    width: 665px; height: 380px;
    background: var(--paper);
    border-radius: 26px;
    overflow: hidden;
    box-shadow: 0 6px 18px rgba(0,0,0,0.18);
  }

  .brand {
    display: flex; align-items: center; gap: 14px;
    color: var(--steel-dark);
    font-weight: 700;
    letter-spacing: 0.5px;
    line-height: 1;
  }
  .brand-dot {
    border: 6px solid var(--blue);
    border-radius: 50%;
    flex: none;
  }

  /* Back of card */
  .card-back {
    display: flex; flex-direction: column; align-items: center; justify-content: center;
    gap: 34px;
  }
  .card-back .brand { font-size: 34px; }
  .card-back .brand-dot { width: 70px; height: 70px; }
  .tagline {
    text-align: center;
    font-weight: 700;
    font-size: 15px;
    line-height: 1.45;
    color: var(--ink);
  }

  /* Front of card */
  .wave { position: absolute; inset: 0; width: 100%; height: 100%; }
  .card-front .brand {
    position: absolute; left: 40px; top: 128px;
    font-size: 36px;
  }
  .card-front .brand-dot { width: 76px; height: 76px; }
  .brand-lines { display: flex; flex-direction: column; gap: 4px; }
  .contact {
    position: absolute; right: 30px; top: 74px;
    text-align: right; color: #fff;
  }
  .contact .name { font-weight: 700; font-size: 18px; letter-spacing: 0.4px; }
  .contact .role { font-size: 14px; margin-bottom: 16px; }
  .contact .address { font-size: 14px; line-height: 1.35; margin-bottom: 6px; }
  .contact ul { list-style: none; font-size: 14px; line-height: 1.55; }
  .contact li { display: flex; justify-content: flex-end; align-items: center; gap: 7px; }
  .contact .icon { width: 15px; height: 15px; flex: none; }
</style>
</head>
<body>
<main class="sheet">

  <section class="card card-back" aria-label="Card back">
    <div class="brand"><span class="brand-dot"></span><span>BRANLEY STEEL</span></div>
    <p class="tagline">Structural Steel - Stainless &amp; Aluminum<br>Building Components - Rebar - Decking.... and more</p>
  </section>

  <section class="card card-front" aria-label="Card front">
    <svg class="wave" viewBox="0 0 665 380" preserveAspectRatio="none" aria-hidden="true">
      <path d="M160 380 C275 378 310 230 352 150 C395 70 460 38 665 38 L665 380 Z" fill="var(--steel-dark)"/>
      <path d="M190 380 C300 380 330 240 370 160 C410 80 470 52 665 50 L665 380 Z" fill="var(--blue)"/>
    </svg>

    <div class="brand">
      <span class="brand-dot"></span>
      <span class="brand-lines"><span>BRANLEY</span><span>STEEL</span></span>
    </div>

    <div class="contact">
      <p class="name">DORIAN WELLBY</p>
      <p class="role">Director</p>
      <p class="address">P.O. Box 5820<br>Harbor Road, Ashford, USA</p>
      <ul>
        <li>555-014-2290
          <svg class="icon" viewBox="0 0 16 16"><circle cx="8" cy="8" r="7" fill="none" stroke="#fff" stroke-width="1.2"/><rect x="4.5" y="6" width="7" height="5" rx="1" fill="#fff"/><rect x="6" y="4" width="4" height="2" fill="#fff"/></svg></li>
        <li>555-014-2291
          <svg class="icon" viewBox="0 0 16 16"><circle cx="8" cy="8" r="7" fill="none" stroke="#fff" stroke-width="1.2"/><rect x="5.5" y="3.5" width="5" height="9" rx="1" fill="none" stroke="#fff" stroke-width="1.2"/></svg></li>
        <li>555-014-2292
          <svg class="icon" viewBox="0 0 16 16"><circle cx="8" cy="8" r="7" fill="none" stroke="#fff" stroke-width="1.2"/><rect x="4" y="6.5" width="8" height="4.5" fill="#fff"/><rect x="5.5" y="4" width="5" height="2.5" fill="none" stroke="#fff"/></svg></li>
        <li>info@branleymail.com
          <svg class="icon" viewBox="0 0 16 16"><circle cx="8" cy="8" r="7" fill="none" stroke="#fff" stroke-width="1.2"/><rect x="4" y="5" width="8" height="6" fill="#fff"/><path d="M4 5 L8 8.5 L12 5" stroke="var(--blue)" fill="none"/></svg></li>
        <li>www.branleysteel.com
          <svg class="icon" viewBox="0 0 16 16"><circle cx="8" cy="8" r="7" fill="none" stroke="#fff" stroke-width="1.2"/><circle cx="8" cy="8" r="4" fill="none" stroke="#fff"/><path d="M4 8 H12 M8 4 V12" stroke="#fff"/></svg></li>
      </ul>
    </div>
  </section>

</main>
</body>
</html>
```